Come crowdsource a Web Design for a brazilian crowdsource Startup!

> NAME OF OUR STARTUP:
Vantremo

> DESCRIPTION OF OUR STARTUP:
We are a crowdsourcing startup in Brazil providing consultancy and technology to support other companies to crowdsource their projects.
We also operate doing big crowdsource campaings related to polemic subjects in Brazil.

> WHAT ARE OUR TARGET AUDIENCE?
Our target audience are young people around 20-35 years old.
Generation Y (Millennial Generation)

> WHAT IS OUR INDUSTRY?
Internet, web

> WHAT DO WE NEED?
We need a Web Design for our first site.

We need 5 pages:
- Home
- What is Crowdsourcing?
- Solutions
- About Us
- Blog
- A box for the "Contact" tab (this is not a page)

Please, find attached a Layout Sketch of what I've imagined.

Lets talk about the sketch:
Well, first of all, it's a SKETCH, so you don't have to send proposals exactly as the sketch. The sketch is just to show how I've imagined the ditribution of the content boxes. For example, the menu bar doesnt need to be a rectangle exactly like the sketch, but, I would like to have the menu on the right side of the logo. Also, you will see that the boxes are all squeezed, of course I dont want them soo squeezed! Again, its juust a SKETCH!

About the images on the sketch:
IMG1 - Some nice and simple image related to collectivity or related to crowdsourcing or maybe use our O logo.

IMG2 - Some simple and creative image related to Consultancy. It doesnt need to be so obvious.

IMG3 - Some simple and creative image related to Web 2.0 Software Technology. It doesnt need to be so obvious.

IMG4 - Some simple and creative image related to a full package of Consultancy + Technology. It doesnt need to be so obvious.

IMG5 - Some nice and simple image related to collectivity or related to crowdsourcing.

IMG6 - Some nice and simple image related to Ideation. Maybe a light bulb? I dont know, be creative!

IMG7 - Some nice and simple image related to Crowdlabor. I dont know, be creative!

IMG8 - Some nice and simple image related to CrowdFeedback. Maybe a megaphone? A loudspeaker? I dont know, be creative!

IMG9 - Some nice and simple image related to us! Maybe our O logo ? I dont know, be creative!

THE CONTACT SIDE BAR - we need a nice and simple contact side bar. By the way, on the sketch this bar is shown only at the homepage, but when the site becomes real this bar will stay along all the pages.

THE CONTACT BOX - we need a nice and simple contact box.

ABOUT THE COLORS TO USE: we would like some color to our background and titles. We like colors similars to our logo: really light blue ? light green/blue ? light grey ? light orange ? I dont know, you guys knows more about that then me =)

PLIMBOOK SHARE/LIKE BUTTON: We would like a plimbook share/like button somewhere on the site!

ABOUT THE ATTACHED FILES:

ADDITIONALS:
> The name Vantremo comes from "collectivity". With our name we want to pass the idea of the collectivity from the crowdsource work model.

> Our communication is directed to the Generation Y.

> Remember, we are a Startup! So we need a modern and simple site, something like the web 2.0 trends. It must be beautiful =)

> We arent a serious company. We are a young and fun company! Please, dont come with old fashionable company sites.

> Be creative =] !

Target Market(s)

Our target audience are young people around 20-35 years old. Generation Y (Millennial Generation)

Industry/Entity Type

Communication

Requirements
Must have
• We need a Web Design for our first site.

We need 5 pages:
- Home
- What is Crowdsourcing?
- Solutions
- About Us
- Blog

ABOUT THE COLORS TO USE: we would like some color to our background and titles. We like colors similars to our logo: really light blue ? light green/blue ? light grey ? light oranges ? I dont know, you guys knows more about that then me =)

Should not have
• Poor/serious/old fashionable designs

```html
<!DOCTYPE html>
<html lang="en">
<head>
<meta charset="utf-8">
<title>Vantremo — Crowdsourcing</title>
<link href="https://fonts.googleapis.com/css2?family=Open+Sans:wght@400;600;700&family=Montserrat:wght@400;500;600&display=swap" rel="stylesheet">
<style>
  :root{
    --teal:#1fa3b5;
    --nav:#2a9fb0;
    --orange:#f26a10;
    --orange-soft:#f6a26b;
    --sand:#f8efe2;
    --text:#555a5f;
    --muted:#8a8f94;
    --line:#d4d7da;
    --white:#ffffff;
    --social:#3a5a98;
    --social-2:#35a9dc;
  }
  *{box-sizing:border-box;margin:0;padding:0}
  html,body{width:1192px;height:1200px;overflow:hidden;background:var(--white)}
  body{position:relative;font-family:"Montserrat",sans-serif;color:var(--text)}
  .abs{position:absolute}

  /* header */
  .hero-band{position:absolute;left:0;top:110px;width:1192px;height:439px;background:var(--sand)}
  .header-sky{position:absolute;left:0;top:0;width:1192px;height:150px}
  .brand{position:absolute;left:140px;top:34px;display:flex;align-items:center;gap:10px;
    font-weight:600;font-size:42px;line-height:52px;color:var(--teal);letter-spacing:-0.5px}
  .brand-dot{width:50px;height:50px;border-radius:50%;background:var(--teal)}
  .main-nav{position:absolute;top:58px;left:0;font-family:"Open Sans",sans-serif;font-weight:600;font-size:17px;color:var(--nav)}
  .main-nav span{position:absolute;white-space:nowrap}

  /* hero */
  .hero-art{position:absolute;left:149px;top:179px;width:334px;height:342px;border-radius:24px;
    background:linear-gradient(160deg,#e3f3f6 0%,#cfe9ef 45%,#f6e6cf 100%)}
  .crowd-art{position:absolute;left:529px;top:153px;width:56px;height:44px;border-radius:10px;
    background:linear-gradient(135deg,#ece2d4,#ddd0bf)}
  .contact-tab{position:absolute;left:435px;top:248px;width:49px;height:143px;background:var(--orange);
    border-radius:6px 0 0 6px;display:flex;align-items:center;justify-content:center}
  .contact-tab span{transform:rotate(-90deg);color:var(--white);font-family:"Open Sans",sans-serif;font-weight:700;font-size:24px}
  .contact-box{position:absolute;left:482px;top:199px;width:708px;height:355px;background:var(--white);
    border:2px solid var(--orange);border-radius:4px}
  .contact-intro{position:absolute;left:47px;top:30px;font-size:19px;line-height:26px;color:var(--teal);font-weight:500}
  .field{position:absolute;left:47px;width:607px;border:1px solid var(--line);border-radius:6px;
    font-size:14px;color:var(--muted);padding:10px 14px}
  .send{position:absolute;left:551px;top:286px;width:103px;height:39px;background:var(--teal);border-radius:5px;
    color:var(--white);font-weight:600;font-size:19px;display:flex;align-items:center;justify-content:center}

  /* services */
  .service{position:absolute;top:591px;width:272px}
  .service-photo{width:272px;height:182px}
  .service-title{margin-top:18px;font-family:"Open Sans",sans-serif;font-weight:700;font-size:18px;color:var(--orange)}
  .service-text{margin-top:8px;font-size:13px;line-height:19.7px;color:var(--text);height:120px;overflow:hidden}
  .service-more{position:absolute;left:0;top:369px;width:272px;height:24px}

  /* footer */
  .footer-rule{position:absolute;left:0;top:1028px;width:1192px;height:3px;background:#d2d4d6}
  .footer-title{position:absolute;top:1055px;font-family:"Open Sans",sans-serif;font-weight:600;font-size:16px;color:#3e4246}
  .contact-label{position:absolute;font-size:13px;line-height:18px;color:var(--muted)}
  .contact-label b{font-weight:500;color:#333}
  .newsletter{position:absolute;left:517px;top:1088px;width:229px;height:30px;background:#ececec;border-radius:4px;
    font-size:13px;color:#555;padding:7px 11px}
  .mail-btn{position:absolute;left:712px;top:1086px;width:34px;height:34px;background:var(--orange);border-radius:3px}
  .social{position:absolute;top:1080px;width:46px;height:45px;border-radius:3px;color:var(--white);
    font-size:8px;font-weight:600;display:flex;align-items:center;justify-content:center}
  .mini-btn{position:absolute;left:972px;height:18px;display:flex;gap:3px;font-size:10px;color:#333}
  .mini-btn .label{border:1px solid #b8c4d0;background:#eef2f7;border-radius:3px;padding:1px 6px}
  .mini-btn .count{border:1px solid #c7c7c7;border-radius:3px;padding:1px 5px;background:var(--white)}

  .footer-band{position:absolute;left:0;top:1151px;width:1192px;height:49px;background:var(--teal)}
  .footer-nav{position:absolute;top:13px;font-family:"Open Sans",sans-serif;font-weight:600;font-size:16px;color:var(--white)}
  .footer-nav span{position:absolute;white-space:nowrap}
  .copyright{position:absolute;left:728px;top:17px;font-size:12px;color:var(--white)}
  .footer-brand{position:absolute;left:955px;top:9px;display:flex;align-items:center;gap:6px;font-weight:600;font-size:24px;color:var(--white)}
  .footer-brand i{width:22px;height:22px;border-radius:50%;background:var(--white);display:block}
</style>
</head>
<body>

<div class="hero-band"></div>

<svg class="header-sky" viewBox="0 0 1192 150" aria-hidden="true">
  <defs>
    <linearGradient id="sky" x1="0" y1="0" x2="0" y2="1">
      <stop offset="0" stop-color="#ffffff"/>
      <stop offset="1" stop-color="#d7f0f7"/>
    </linearGradient>
  </defs>
  <path d="M0 0H1192V134C900 150 300 150 0 114Z" fill="url(#sky)"/>
  <path d="M0 114C300 150 900 150 1192 134" fill="none" stroke="#1fa3b5" stroke-width="3"/>
</svg>

<div class="brand"><span class="brand-dot"></span>Vantremo</div>

<nav class="main-nav">
  <span style="left:582px">What is Crowdsourcing?</span>
  <span style="left:807px">Solutions</span>
  <span style="left:913px">About Us</span>
  <span style="left:1016px">Blog</span>
</nav>

<div class="hero-art" role="img" aria-label="Illustration of a large speech bubble filled with colourful dots, with a crowd of people icons gathered at its lower right"></div>
<div class="crowd-art" role="img" aria-label="Small cluster of people icons"></div>

<div class="contact-tab"><span>Contact</span></div>

<section class="contact-box">
  <p class="contact-intro">Get in touch with us right now!<br>For questions, prices, or just to chat, we are here to listen you.</p>
  <div class="field" style="top:93px;height:39px">Your e-mail</div>
  <div class="field" style="top:142px;height:39px">Subject</div>
  <div class="field" style="top:191px;height:86px">Message</div>
  <div class="send">Send</div>
</section>

<article class="service" style="left:140px">
  <div class="service-photo" role="img" aria-label="Photo of a consultant reviewing documents with clients" style="background:linear-gradient(135deg,#dfe8ee,#9fb3c2)"></div>
  <h3 class="service-title">Consultancy</h3>
  <p class="service-text">Here we have a short description of our Consultancy service. Lorem ipsum dolor sit amet, consectetur adipiscing elit. Vestibulum lectus ante, lacinia eu ultrices non, pellentesque at elit. Proin malesuada pellentesque libero a consectetur. Proin</p>
  <svg class="service-more" viewBox="0 0 272 24" aria-hidden="true"><line x1="0" y1="0.5" x2="272" y2="0.5" stroke="#f6a26b"/><path d="M100 0H172L136 22Z" fill="#f6a26b"/><path d="M131 7H141M136 2V12" stroke="#fff" stroke-width="2"/></svg>
</article>

<article class="service" style="left:460px">
  <div class="service-photo" role="img" aria-label="Photo of a hand touching a glowing digital network interface" style="background:linear-gradient(135deg,#4a4d52,#151618)"></div>
  <h3 class="service-title">Techonlogy</h3>
  <p class="service-text">Here we have a short description of our Consultancy service. Lorem ipsum dolor sit amet, consectetur adipiscing elit. Vestibulum lectus ante, lacinia eu ultrices non, pellentesque at elit. Proin malesuada pellentesque libero a consectetur. Proin</p>
  <svg class="service-more" viewBox="0 0 272 24" aria-hidden="true"><line x1="0" y1="0.5" x2="272" y2="0.5" stroke="#f6a26b"/><path d="M100 0H172L136 22Z" fill="#f6a26b"/><path d="M131 7H141M136 2V12" stroke="#fff" stroke-width="2"/></svg>
</article>

<article class="service" style="left:783px">
  <div class="service-photo" role="img" aria-label="Photo of a person sketching a network of people around a chat bubble" style="background:linear-gradient(135deg,#f4f6f7,#cfe3ea)"></div>
  <h3 class="service-title">Consultancy + Technology</h3>
  <p class="service-text">Here we have a short description of our Consultancy service. Lorem ipsum dolor sit amet, consectetur adipiscing elit. Vestibulum lectus ante, lacinia eu ultrices non, pellentesque at elit. Proin malesuada pellentesque libero a consectetur. Proin</p>
  <svg class="service-more" viewBox="0 0 272 24" aria-hidden="true"><line x1="0" y1="0.5" x2="272" y2="0.5" stroke="#f6a26b"/><path d="M100 0H172L136 22Z" fill="#f6a26b"/><path d="M131 7H141M136 2V12" stroke="#fff" stroke-width="2"/></svg>
</article>

<div class="footer-rule"></div>

<h4 class="footer-title" style="left:140px">BE IN TOUCH</h4>
<svg class="abs" style="left:141px;top:1092px" width="26" height="28" viewBox="0 0 26 28" aria-hidden="true">
  <path d="M4 3L9 2L12 9L9 11C10 15 13 19 17 21L19 18L25 22L23 26C13 26 3 15 4 3Z" fill="none" stroke="#1fa3b5" stroke-width="2.2" stroke-linejoin="round"/>
</svg>
<p class="contact-label" style="left:174px;top:1088px">Phone:<br>(555) 214-7730</p>
<svg class="abs" style="left:308px;top:1094px" width="24" height="18" viewBox="0 0 24 18" aria-hidden="true">
  <rect x="1" y="1" width="22" height="16" fill="none" stroke="#1fa3b5" stroke-width="2"/>
  <path d="M1 1L12 10L23 1M1 17L9 9M23 17L15 9" fill="none" stroke="#1fa3b5" stroke-width="1.6"/>
</svg>
<p class="contact-label" style="left:341px;top:1086px">Email:<br><b>info@vantremo.com</b></p>

<h4 class="footer-title" style="left:515px">NEWSLETTER</h4>
<div class="newsletter">Enter your email address</div>
<div class="mail-btn" aria-label="Subscribe"></div>

<h4 class="footer-title" style="left:816px">FOLLOW US</h4>
<div class="social" style="left:814px;background:var(--social)">plimbook</div>
<div class="social" style="left:867px;background:var(--social-2)">chirpnet</div>
<div class="mini-btn" style="top:1081px"><span class="label">Share</span><span class="count">12</span></div>
<div class="mini-btn" style="top:1107px"><span class="label">Like</span><span class="count">8</span></div>

<footer class="footer-band">
  <nav class="footer-nav">
    <span style="left:140px">What is Crowdsourcing?</span>
    <span style="left:339px">Solutions</span>
    <span style="left:432px">About Us</span>
    <span style="left:525px">Blog</span>
  </nav>
  <p class="copyright">© 2013 Vantremo. All rights reserved.</p>
  <div class="footer-brand"><i></i>Vantremo</div>
</footer>

</body>
</html>
```